Amber Reed Properties, which offers a selection of prime properties (villas

A website that contains: Idea, benefits, destinations (villas), offers, about us, contact, newsletter, social media, blog, look at the attachment, even if it is in German. The idea is that I can easily add new pages, if necessary, with the design you make. Later on we want to add a reservation system, so you can book your villa through the internet. Besides, there is a concierge service available, which organizes everything for the customer, owner, from villa to restaurant, limo service, ... & benefits and emotions through nice pictures / videos, they should be convinced to invest.

Target Market(s)

Investors (golfer and non-golfer) which have 300'000 to invest in a kind of real-estate investing club

Number of Pages Required

5+ page

Font styles to use
Sans Serif

Requirements
Must have
• It must be for wordpress, must have an exclusive touch, high quality, with nice pictures of golf courses. The Logo is gold so it has to match with gold, the font is segan or segoe semilight or similar, sans serif
Nice to have
• may be as well as the possibility to include videos of the different destinations and houses

```html
<!DOCTYPE html>
<html lang="de">
<head>
<meta charset="utf-8">
<title>Amber Reed Properties – Ihr Nutzen</title>
<link rel="stylesheet" href="https://fonts.googleapis.com/css2?family=Mulish:wght@300;400&display=swap">
<style>
  :root {
    --black: #000000;
    --gold: #e6a800;
    --amber: #ffb400;
    --ink: #111111;
    --muted: #cfcfcf;
    --bar: #1c1c1c;
  }
  * { margin: 0; padding: 0; box-sizing: border-box; }
  html, body { width: 770px; height: 1200px; overflow: hidden; background: var(--black); }
  body { font-family: "Mulish", sans-serif; position: relative; color: var(--gold); }

  .site-header { position: absolute; top: 0; left: 0; width: 770px; height: 65px; }
  .nav a { position: absolute; top: 34px; font-size: 8px; font-weight: 300; color: var(--gold); text-decoration: none; letter-spacing: 0.2px; transform: translateY(-50%); white-space: nowrap; }
  .brand { position: absolute; left: 0; width: 770px; text-align: center; font-size: 8px; font-weight: 400; color: var(--gold); letter-spacing: 0.3px; }
  .brand .mark { display: block; width: 12px; height: 12px; margin: 0 auto 4px; border: 1.2px solid var(--gold); }

  .hero { position: absolute; top: 65px; left: 0; width: 770px; height: 270px;
    background: linear-gradient(180deg, #3b8fe0 0%, #7fb7ea 30%, #e8b64a 55%, #3f6e2a 80%, #2a4f1e 100%); }

  .section-title { position: absolute; top: 380px; left: 0; width: 770px; text-align: center; font-size: 24px; font-weight: 300; color: var(--gold); letter-spacing: 0.3px; }

  .photo-pool { position: absolute; top: 456px; left: 0; width: 402px; height: 188px;
    background: linear-gradient(180deg, #6f86b0 0%, #c9a27a 35%, #9a6a3c 55%, #2f6fc8 75%, #1d56b0 100%); }
  .panel { position: absolute; background: var(--amber); color: var(--ink); font-size: 10.4px; font-weight: 400; line-height: 14.2px; }
  .panel-one { top: 456px; left: 402px; width: 260px; height: 188px; padding: 40px 20px 0 28px; }

  .panel-two { top: 701px; left: 108px; width: 260px; height: 228px; padding: 14px 24px 0 10px; text-align: right; }
  .panel-two h3 { font-size: 10.4px; font-weight: 400; margin-bottom: 12px; letter-spacing: 0.2px; }
  .photo-golf { position: absolute; top: 701px; left: 368px; width: 402px; height: 189px;
    background: linear-gradient(180deg, #b8c9d8 0%, #6f8f6a 18%, #3f7a34 45%, #4f7f95 62%, #4a9a3a 80%, #2f6e27 100%); }

  .site-footer { position: absolute; top: 1010px; left: 0; width: 770px; }
  .footer-nav { position: absolute; top: 60px; left: 0; width: 770px; text-align: center; font-size: 8px; font-weight: 300; }
  .footer-nav a { color: var(--gold); text-decoration: none; margin: 0 10px; }
  .address { position: absolute; top: 82px; left: 0; width: 770px; text-align: center; font-size: 7.6px; line-height: 11px; color: var(--muted); font-weight: 300; }
  .social { position: absolute; top: 123px; left: 0; width: 770px; display: flex; justify-content: center; gap: 10px; }
  .social span { width: 15px; height: 15px; background: var(--amber); border-radius: 2px; display: block; }
  .legal { position: absolute; top: 1166px; left: 0; width: 770px; height: 17px; background: var(--bar); text-align: center; font-size: 7px; line-height: 17px; color: var(--gold); font-weight: 300; letter-spacing: 0.2px; }
</style>
</head>
<body>
  <header class="site-header">
    <nav class="nav">
      <a href="#" style="left:109px">IDEA</a>
      <a href="#" style="left:149px">BENEFITS</a>
      <a href="#" style="left:207px">DESTINATIONS (VILLAS)</a>
      <a href="#" style="left:477px">OFFERS</a>
      <a href="#" style="left:529px">ABOUT US</a>
      <a href="#" style="left:591px">CONTACT US</a>
    </nav>
    <div class="brand" style="top:16px"><span class="mark"></span>AMBER REED PROPERTIES</div>
  </header>

  <div class="hero" role="img" aria-label="Gelbe Villa mit Terrakottadach zwischen Palmen unter blauem Himmel"></div>

  <h2 class="section-title">IHR NUTZEN – EMOTIONAL</h2>

  <div class="photo-pool" role="img" aria-label="Resortanlage mit Pool, blauen Liegen und Palmen in der Abenddämmerung"></div>
  <div class="panel panel-one">
    Sie sind Mitbesitzer von exklusiven Immobilien in Topresorts, in wunderschöner, gepflegter und sicherer Umgebung Miteigentum ermöglicht Ihnen, Ihre Ferien an verschiedenen Destinationen zu verbringen.<br>
    – Abwechslung ist garantiert
  </div>

  <div class="panel panel-two">
    <h3>SIE GENIESSEN:</h3>
    die Privatsphäre in ihren Traumvillen,<br>
    weltweit, mit Familie und Freunden<br>
    das Spiel auf Top-Golfplätzen und dem<br>
    Zugang zu privaten Anlagen den Besuch<br>
    der Sehenswürdigkeiten<br>
    «Shop until you drop»<br>
    Kulinarische Highlights in<br>
    Insider-Restaurants. Aufregendes Nightlife<br>
    in den angesagtesten Clubs Sie fördern die<br>
    nachhaltige Nutzung von Immobilien<br>
    Sie erhalten eine unbezahlbare<br>
    «Erlebnisrendite»
  </div>
  <div class="photo-golf" role="img" aria-label="Luftaufnahme eines Golfplatzes mit See und grünen Fairways"></div>

  <footer class="site-footer">
    <div class="brand" style="top:6px"><span class="mark"></span>AMBER REED PROPERTIES</div>
    <nav class="footer-nav">
      <a href="#">IDEA</a><a href="#">BENEFITS</a><a href="#">DESTINATIONS (VILLAS)</a><a href="#">OFFERS</a><a href="#">ABOUT US</a><a href="#">CONTACT US</a>
    </nav>
    <address class="address" style="font-style:normal">
      C/O Fairway Circle GmbH Lindenweg 14 CH-8700 Küsnacht Zurich / Switzerland<br>
      +41 44 000 12 34, +41 76 000 56 78<br>
      info@fairwaycircle.ch
    </address>
    <div class="social" aria-label="Social media">
      <span></span><span></span><span></span><span></span><span></span>
    </div>
  </footer>
  <div class="legal">ALL RIGHTS RESERVED</div>
</body>
</html>
```